Seed Company Looking For a Soybean Seed Bag Design

We are are a regional seed company who is currently launching a new line of soybean products. The brand of the product will be Tru-Vora. We are looking for a custom design of a soybean bag measuring 16"x5"x30" (when constructed). We are looking for a modern design that's relatively loud, but not too busy. The proof needs to match with the attached template. We have also provided a proof of a previous bag project (Fox-Brook-Standard) we've done to show how the artwork needs to be laid out. In no way does the new design need to resemble the example. Also attached are some other examples of seed bags.
Agriculture
Designer to choose colors to be used in the design.

```html
<!DOCTYPE html>
<html lang="en">
<head>
<meta charset="utf-8">
<title>Tru-Vora Soybean Seed Bag Dieline</title>
<link rel="stylesheet" href="https://fonts.googleapis.com/css2?family=Montserrat:wght@600;700;800&family=Libre+Baskerville&family=Roboto+Condensed:wght@400&display=swap">
<style>
  :root {
    --bag-green: #129c48;
    --brand-green: #1f9a47;
    --charcoal: #3f3f41;
    --mid-grey: #5b5b5d;
    --paper: #ffffff;
    --dim-grey: #333333;
    --dim-blue: #1a8fd6;
  }
  html, body {
    margin: 0;
    padding: 0;
    width: 918px;
    height: 1200px;
    overflow: hidden;
    background: var(--paper);
  }
  .dieline {
    position: absolute;
    left: 0;
    top: 263px;
    width: 918px;
    height: 674px;
    display: block;
  }
  .wordmark { font-family: "Montserrat", sans-serif; font-weight: 800; fill: var(--brand-green); letter-spacing: 2px; }
  .slogan { font-family: "Montserrat", sans-serif; font-weight: 600; fill: var(--mid-grey); letter-spacing: 1px; }
  .product-title { font-family: "Montserrat", sans-serif; font-weight: 700; letter-spacing: 1px; }
  .product-title.on-dark { fill: var(--paper); }
  .product-title.on-light { fill: var(--charcoal); }
  .quality-pill-text { font-family: "Libre Baskerville", serif; }
  .contact { font-family: "Roboto Condensed", sans-serif; fill: var(--paper); }
  .dim-label { font-family: "Roboto Condensed", sans-serif; font-size: 15px; }
  .dim-label.outer { fill: var(--dim-grey); }
  .dim-label.inner { fill: var(--dim-blue); }
  .dim-line.outer { stroke: #9a9a9a; stroke-width: 1; fill: none; }
  .dim-line.inner { stroke: var(--dim-blue); stroke-width: 1; fill: none; }
</style>
</head>
<body>
<svg class="dieline" viewBox="30 1050 1540 1130" xmlns="http://www.w3.org/2000/svg">
  <defs>
    <linearGradient id="dot-fade-top" x1="0" y1="0" x2="0" y2="1">
      <stop offset="0" stop-color="#444446" stop-opacity="0.75"/>
      <stop offset="1" stop-color="#444446" stop-opacity="0"/>
    </linearGradient>
    <linearGradient id="dot-fade-green" x1="0" y1="0" x2="0" y2="1">
      <stop offset="0" stop-color="#1f9a47" stop-opacity="0"/>
      <stop offset="1" stop-color="#1f9a47" stop-opacity="0.7"/>
    </linearGradient>
    <linearGradient id="dot-fade-bottom" x1="0" y1="0" x2="0" y2="1">
      <stop offset="0" stop-color="#444446" stop-opacity="0"/>
      <stop offset="1" stop-color="#444446" stop-opacity="0.75"/>
    </linearGradient>
  </defs>

  <rect class="bag-field" x="127" y="1077" width="1425" height="993" fill="var(--bag-green)"/>

  <!-- left gusset -->
  <g class="gusset gusset-left">
    <rect x="268" y="1153" width="150" height="842" fill="var(--paper)"/>
    <rect x="268" y="1153" width="150" height="107" fill="url(#dot-fade-top)" role="img" aria-label="Fading halftone dot pattern"/>
    <g transform="translate(345,1460) rotate(90)">
      <text class="wordmark" x="0" y="0" font-size="50" text-anchor="middle" dominant-baseline="central">TRU-VORA</text>
      <text class="slogan" x="0" y="40" font-size="10" text-anchor="middle" dominant-baseline="central">GROWN STRONG, SEASON AFTER SEASON</text>
    </g>
    <line x1="295" y1="1683" x2="340" y2="1683" stroke="var(--charcoal)" stroke-width="2"/>
    <line x1="340" y1="1683" x2="385" y2="1683" stroke="var(--brand-green)" stroke-width="2"/>
    <g transform="translate(355,1800) rotate(90)">
      <text class="product-title on-light" x="0" y="-15" font-size="28" text-anchor="middle" dominant-baseline="central">SOYBEAN</text>
      <text class="product-title on-light" x="0" y="13" font-size="28" text-anchor="middle" dominant-baseline="central">—SEED—</text>
      <rect x="-48" y="37" width="96" height="20" rx="10" fill="var(--charcoal)"/>
      <text class="quality-pill-text" x="0" y="47" font-size="10" fill="var(--paper)" text-anchor="middle" dominant-baseline="central">Premium Quality</text>
    </g>
    <path d="M290 1995 V1983 Q290 1975 300 1975 H385 Q395 1975 395 1983 V1995 Z" fill="var(--charcoal)"/>
  </g>

  <!-- front panel -->
  <g class="panel panel-front">
    <rect x="450" y="1153" width="481" height="842" fill="var(--paper)"/>
    <rect x="450" y="1153" width="481" height="210" fill="url(#dot-fade-top)" role="img" aria-label="Fading halftone dot pattern"/>
    <rect x="450" y="1890" width="72" height="105" fill="url(#dot-fade-green)" role="img" aria-label="Green halftone dot pattern"/>
    <rect x="860" y="1890" width="71" height="105" fill="url(#dot-fade-green)" role="img" aria-label="Green halftone dot pattern"/>
    <text class="wordmark" x="690" y="1570" font-size="62" text-anchor="middle" dominant-baseline="central">TRU-VORA</text>
    <text class="slogan" x="690" y="1640" font-size="11.5" text-anchor="middle" dominant-baseline="central">GROWN STRONG, SEASON AFTER SEASON</text>

    <path class="product-label" d="M522 1995 V1768 Q522 1745 548 1738 Q690 1712 834 1738 Q860 1745 860 1768 V1995 Z" fill="var(--charcoal)"/>
    <text class="product-title on-dark" x="691" y="1785" font-size="38" text-anchor="middle" dominant-baseline="central">SOYBEAN</text>
    <text class="product-title on-dark" x="691" y="1820" font-size="38" text-anchor="middle" dominant-baseline="central">SEED</text>
    <line x1="586" y1="1820" x2="632" y2="1820" stroke="var(--paper)" stroke-width="2"/>
    <line x1="750" y1="1820" x2="796" y2="1820" stroke="var(--paper)" stroke-width="2"/>
    <rect x="623" y="1852" width="136" height="26" rx="13" fill="var(--paper)"/>
    <text class="quality-pill-text" x="691" y="1865" font-size="13" fill="var(--charcoal)" text-anchor="middle" dominant-baseline="central">Premium Quality</text>
    <text class="contact" x="691" y="1905" font-size="12" text-anchor="middle" dominant-baseline="central">Fox-Brook-Standard</text>
    <text class="contact" x="691" y="1919" font-size="12" text-anchor="middle" dominant-baseline="central">412 Mill Road | Fox Brook, WI 54021</text>
    <text class="contact" x="691" y="1933" font-size="12" text-anchor="middle" dominant-baseline="central">800-555-0142 | sales@fbsseed.com</text>
    <text class="contact" x="691" y="1948" font-size="12" text-anchor="middle" dominant-baseline="central">www.FoxBrookSeed.com</text>
  </g>

  <!-- right gusset -->
  <g class="gusset gusset-right">
    <rect x="964" y="1153" width="150" height="842" fill="var(--paper)"/>
    <rect x="964" y="1153" width="150" height="107" fill="url(#dot-fade-top)" role="img" aria-label="Fading halftone dot pattern"/>
    <g transform="translate(1035,1355) rotate(-90)">
      <text class="product-title on-light" x="0" y="-25" font-size="28" text-anchor="middle" dominant-baseline="central">SOYBEAN</text>
      <text class="product-title on-light" x="0" y="5" font-size="28" text-anchor="middle" dominant-baseline="central">—SEED—</text>
      <rect x="-48" y="27" width="96" height="20" rx="10" fill="var(--charcoal)"/>
      <text class="quality-pill-text" x="0" y="37" font-size="10" fill="var(--paper)" text-anchor="middle" dominant-baseline="central">Premium Quality</text>
    </g>
    <line x1="997" y1="1468" x2="1041" y2="1468" stroke="var(--brand-green)" stroke-width="2"/>
    <line x1="1041" y1="1468" x2="1086" y2="1468" stroke="var(--charcoal)" stroke-width="2"/>
    <g transform="translate(1038,1690) rotate(-90)">
      <text class="wordmark" x="0" y="0" font-size="50" text-anchor="middle" dominant-baseline="central">TRU-VORA</text>
      <text class="slogan" x="0" y="34" font-size="10" text-anchor="middle" dominant-baseline="central">GROWN STRONG, SEASON AFTER SEASON</text>
    </g>
    <path d="M986 1995 V1983 Q986 1975 996 1975 H1081 Q1091 1975 1091 1983 V1995 Z" fill="var(--charcoal)"/>
  </g>

  <!-- back panel -->
  <g class="panel panel-back">
    <rect x="1229" y="1153" width="315" height="842" fill="var(--paper)"/>
    <rect x="1229" y="1885" width="315" height="110" fill="url(#dot-fade-bottom)" role="img" aria-label="Halftone dot pattern rising from the base"/>
  </g>

  <!-- dimensions -->
  <g class="dimensions">
    <path class="dim-line outer" d="M83 1077 V1545 M83 1601 V2070 M83 1077 H120 M83 2070 H120"/>
    <text class="dim-label outer" transform="translate(83,1573) rotate(90)" text-anchor="middle" dominant-baseline="central">▸ 30" ◂</text>
    <path class="dim-line inner" d="M50 1153 V1530 M50 1616 V1995 M50 1153 H120 M50 1995 H120"/>
    <text class="dim-label inner" transform="translate(50,1573) rotate(90)" text-anchor="middle" dominant-baseline="central">▸ 25.375" ◂</text>

    <path class="dim-line outer" d="M127 2080 V2115 M260 2080 V2115 M268 2080 V2115 M418 2080 V2115 M426 2080 V2115 M931 2080 V2115 M956 2080 V2115 M1114 2080 V2115 M1122 2080 V2115 M1552 2080 V2115"/>
    <text class="dim-label outer" x="193" y="2120" text-anchor="middle">▸ 4" ◂</text>
    <text class="dim-label outer" x="343" y="2120" text-anchor="middle">▸ 5" ◂</text>
    <text class="dim-label outer" x="690" y="2120" text-anchor="middle">▸ 16" ◂</text>
    <text class="dim-label outer" x="1039" y="2120" text-anchor="middle">▸ 5" ◂</text>
    <text class="dim-label outer" x="1337" y="2120" text-anchor="middle">▸ 13" ◂</text>

    <path class="dim-line inner" d="M268 2130 V2148 M418 2130 V2148 M450 2130 V2148 M931 2130 V2148 M964 2130 V2148 M1114 2130 V2148 M1229 2130 V2148 M1544 2130 V2148"/>
    <text class="dim-label inner" x="343" y="2152" text-anchor="middle">▸ 4.5" ◂</text>
    <text class="dim-label inner" x="690" y="2152" text-anchor="middle">▸14.5" ◂</text>
    <text class="dim-label inner" x="1039" y="2152" text-anchor="middle">▸ 4.5" ◂</text>
    <text class="dim-label inner" x="1386" y="2152" text-anchor="middle">▸ 9.5" ◂</text>
  </g>
</svg>
</body>
</html>
```